Letterhead for small civil engineer company

We need bold and modern design for company letterhead in MS word. It needs to have company logo and company info. Somewhere in the upper right part of document needs to be space for "recever" and the documents starts with, example, "SUBJECT: CIVIL ENGINEER LETTERHEAD".

in the bottom part of document needs to be signature and date.

Company info: Veltrana d.o.o., Lipovac 15, Lipovac (Općina Brdarić), OIB 47396028154, www.veltrana.hr, info@veltrana.hr

Email of document sender needs to be somewhere if document, exapmle xyz@veltrana.hr

Target Market(s)

Civil engineer company and projects

Industry/Entity Type

Civil engineer

Font styles to use
Serif

Colors
F0912C
F2A743
F7CA91
FBE8D2
FDF5EE

Requirements
Must have
• Company logo and company info
Nice to have
• Moder and clean design
Should not have
• Too much details

```html
<!DOCTYPE html>
<html lang="hr">
<head>
<meta charset="utf-8">
<title>Veltrana d.o.o. – Letterhead</title>
<link href="https://fonts.googleapis.com/css2?family=Poppins:wght@300;400;500;600;700&display=swap" rel="stylesheet">
<style>
  :root {
    --orange: #F0912C;
    --orange-soft: #F2A743;
    --peach: #F7CA91;
    --cream: #FBE8D2;
    --ivory: #FDF5EE;
    --ink: #1b1b1b;
    --muted: #555;
    --backdrop: #cdd3d2;
    --paper: #ffffff;
  }
  * { box-sizing: border-box; margin: 0; padding: 0; }
  html, body { width: 1200px; height: 686px; overflow: hidden; }
  body {
    background: var(--backdrop);
    font-family: "Poppins", sans-serif;
    color: var(--ink);
    position: relative;
  }
  .letterhead {
    position: absolute;
    left: 370px; top: 18px;
    width: 460px; height: 650px;
    background: var(--paper);
    box-shadow: 0 6px 18px rgba(0,0,0,.12);
    padding: 30px 34px 24px;
    display: flex; flex-direction: column;
  }
  .masthead {
    display: flex; justify-content: space-between; align-items: flex-end;
    padding-bottom: 12px;
    border-bottom: 1.5px solid var(--orange);
  }
  .brand { display: flex; align-items: center; gap: 8px; }
  .brand-square { width: 14px; height: 14px; border: 2px solid var(--orange); }
  .brand-name {
    font-size: 22px; font-weight: 400; letter-spacing: 1px;
    color: var(--orange);
  }
  .receiver { line-height: 1.1; }
  .receiver-label { color: var(--orange); font-weight: 600; font-size: 13px; }
  .person-name { font-size: 15px; }
  .person-name b { font-weight: 700; }
  .person-name span { font-weight: 300; }
  .person-role { font-size: 7.5px; font-weight: 400; }

  .subject { margin-top: 14px; font-size: 8px; font-weight: 600; }
  .subject em { font-style: normal; color: var(--orange); }
  .letter-date { margin-top: 6px; font-size: 7px; }
  .addressee { margin-top: 3px; line-height: 1.1; }
  .addressee .person-name { font-size: 16px; }

  .letter-body { margin-top: 12px; font-size: 8.5px; line-height: 1.6; }
  .letter-body p + p { margin-top: 14px; }

  .sign-off {
    margin-top: auto; align-self: flex-end;
    width: 190px; position: relative; padding-top: 44px;
    font-size: 8px; line-height: 1.4;
  }
  .signature {
    position: absolute; top: 0; left: -20px;
    width: 170px; height: 46px; border-radius: 23px;
    background: linear-gradient(90deg, var(--ivory), var(--cream) 50%, var(--ivory));
  }
  .sign-off .title { font-weight: 400; font-size: 7px; }
  .sign-off .date, .sign-off .email { font-weight: 500; }

  .contact-bar {
    margin-top: 16px; padding-top: 10px;
    border-top: 1.5px solid var(--orange);
    font-size: 8px; font-weight: 500;
    display: grid; grid-template-columns: 1.6fr 1fr; row-gap: 6px;
  }
  .contact-item { display: flex; align-items: center; gap: 5px; }
  .contact-item svg { width: 10px; height: 10px; flex: none; fill: none; stroke: var(--orange); stroke-width: 1.6; }
</style>
</head>
<body>
  <main class="letterhead">
    <header class="masthead">
      <div class="brand">
        <span class="brand-square"></span>
        <span class="brand-name">VELTRANA</span>
      </div>
      <div class="receiver">
        <div class="receiver-label">Recever</div>
        <div class="person-name"><b>Marta</b> <span>Kovač</span></div>
        <div class="person-role">Founder &amp; CEO</div>
      </div>
    </header>

    <div class="subject"><em>SUBJECT:</em> CIVIL ENGINEER LETTERHEAD</div>
    <div class="letter-date">August-05-2019</div>
    <div class="addressee">
      <div class="person-name"><b>Marta</b> <span>Kovač</span></div>
      <div class="person-role">Founder &amp; CEO</div>
    </div>

    <section class="letter-body">
      <p>Lorem ipsum dolor sit amet, consectetuer adipiscing elit, sed diam nonummy nibh euismod tincidunt ut laoreet dolore magna aliquam erat volutpat. Ut wisi enim ad minim veniam, quis nostrud exerci tation ullamcorper suscipit lobortis nisl ut aliquip ex ea commodo consequat. Duis autem vel eum iriure dolor in hendrerit in vulputate velit esse molestie consequat, vel illum dolore eu feugiat nulla facilisis at vero eros et accumsan et iusto odio dignissim qui blandit praesent luptatum zzril delenit augue duis dolore te feugait nulla facilisi.</p>
      <p>Lorem ipsum dolor sit amet, cons ectetuer adipiscing elit, sed diam nonummy nibh euismod tincidunt ut laoreet dolore magna aliquam erat volutpat. Ut wisi enim ad minim veniam, quis nostrud exerci tation ullamcorper suscipit lobortis nisl ut aliquip ex ea commodo consequat.</p>
      <p>Lorem ipsum dolor sit amet, consectetuer adipiscing elit, sed diam nonummy nibh euismod tincidunt ut laoreet dolore magna aliquam</p>
    </section>

    <div class="sign-off">
      <div class="signature" role="img" aria-label="Handwritten signature of Ivan Perić"></div>
      <div class="title">Co-Founder</div>
      <div class="date">Date: 14/12/2024</div>
      <div class="email">xyz@veltrana.hr</div>
    </div>

    <footer class="contact-bar">
      <div class="contact-item">
        <svg viewBox="0 0 10 10"><path d="M5 9.2C2.6 6.6 1.8 5.1 1.8 3.8a3.2 3.2 0 0 1 6.4 0c0 1.3-.8 2.8-3.2 5.4z"/><circle cx="5" cy="3.8" r="1.1"/></svg>
        Veltrana d.o.o., Lipovac 15, Lipovac (Općina Brdarić)
      </div>
      <div class="contact-item">
        <svg viewBox="0 0 10 10"><circle cx="5" cy="5" r="4"/><path d="M1 5h8M5 1c-2 2.4-2 5.6 0 8M5 1c2 2.4 2 5.6 0 8"/></svg>
        www.veltrana.hr
      </div>
      <div class="contact-item">
        <svg viewBox="0 0 10 10"><path d="M2 1.2l1.8 0 .8 2-1.2.8a5 5 0 0 0 2.6 2.6l.8-1.2 2 .8v1.8c0 .5-.4.8-.9.8A7.8 7.8 0 0 1 1.2 2.1c0-.5.3-.9.8-.9z"/></svg>
        OIB 47396028154
      </div>
      <div class="contact-item">
        <svg viewBox="0 0 10 10"><rect x="1" y="2.2" width="8" height="5.6" rx=".6"/><path d="M1.2 2.6L5 5.6l3.8-3"/></svg>
        info@veltrana.hr
      </div>
    </footer>
  </main>
</body>
</html>
```